Dynamic Templates

Our company hosts web stores for our clients. They can set up as many as they wish on our platform, and select from the stock templates we provide. We are looking to increase the number of available stock templates.

Because our users can dynamically control many of the template elements - specifically colors - they have to be flexible and abide by certain rules. These rules are spelled out in the attached documents.

Here are links to two of our most used templates:
http://fernridge.vexalcart.example/
http://stampled.vexalcart.example/

Templates need to have a landing page (what you see when first clicking one of the above links). There also needs to be a category page (what you see when clicking any category) and a product detail page (what you see when you arrive at an individual product, where there are various cart options like Buy Now or Request Info).

```html
<!DOCTYPE html>
<html lang="en">
<head>
<meta charset="utf-8">
<title>BrightCrate Supply – Promotional Products</title>
<link rel="stylesheet" href="https://fonts.googleapis.com/css2?family=Arimo:wght@400;700&family=Didact+Gothic&display=swap">
<style>
  :root {
    --topbar-bg: #e5e5e5;
    --header-bg: #f3f3f3;
    --stage-dark: #1b1b1b;
    --stage-dark-top: #2b2b2b;
    --banner-top: #0a86c2;
    --banner-bottom: #003d6b;
    --ink: #1f1f1f;
    --body-ink: #3a3a3a;
    --brand-navy: #123a66;
    --accent: #f7941d;
    --footer-bg: #232323;
    --footer-deep: #111111;
    --footer-link: #e8e8e8;
    --footer-rule: #3c3c3c;
    --panel-bg: #121212;
    --panel-border: #353535;
  }
  * { box-sizing: border-box; margin: 0; padding: 0; }
  html, body { width: 1200px; height: 1168px; overflow: hidden; }
  body { position: relative; background: #fff; font-family: "Arimo", Arial, sans-serif; color: var(--ink); }
  a { color: inherit; text-decoration: none; }

  .topbar { position: absolute; left: 0; top: 0; width: 1200px; height: 32px; background: var(--topbar-bg); border-bottom: 1px solid #cfcfcf; }
  .topbar__contact { position: absolute; right: 145px; top: 7px; font-family: "Didact Gothic", sans-serif; font-size: 15px; color: #222; }

  .header { position: absolute; left: 0; top: 32px; width: 1200px; height: 100px; background: var(--header-bg); }
  .brand { position: absolute; left: 124px; top: 12px; display: flex; align-items: center; gap: 8px; }
  .brand__dot { width: 66px; height: 66px; border-radius: 50%; background: var(--accent); }
  .brand__name { font-family: "Arimo", sans-serif; font-weight: 700; font-size: 28px; color: var(--brand-navy); letter-spacing: -0.3px; }

  .stage { position: absolute; left: 0; top: 132px; width: 1200px; height: 226px; background: linear-gradient(var(--stage-dark-top), var(--stage-dark)); }
  .banner { position: absolute; left: 124px; top: 179px; width: 930px; height: 329px; background: linear-gradient(var(--banner-top), var(--banner-bottom)); }
  .banner__shelf { position: absolute; left: 68px; top: 70px; width: 794px; height: 200px; background: linear-gradient(#e9e9e9, #cfd8e0 75%, rgba(255,255,255,0.15)); opacity: 0.85; }
  .banner__shadow { position: absolute; left: 124px; top: 504px; width: 930px; height: 28px; background: radial-gradient(ellipse at 50% 0%, rgba(0,0,0,0.55), rgba(0,0,0,0) 70%); }

  .intro { position: absolute; left: 126px; top: 563px; width: 720px; }
  .intro__title { font-family: "Didact Gothic", sans-serif; font-weight: 400; font-size: 24px; color: var(--ink); margin-bottom: 22px; }
  .intro__text { font-size: 12px; line-height: 15px; color: var(--body-ink); letter-spacing: 0.4px; margin: 0 0 13px 6px; }
  .intro__title--second { margin-top: 28px; margin-bottom: 26px; }

  .cta { position: absolute; left: 824px; top: 556px; width: 234px; height: 82px; background: repeating-linear-gradient(45deg, #f2f2f2 0 2px, #e8e8e8 2px 4px); }
  .cta__button { position: absolute; left: 22px; top: 18px; width: 190px; height: 42px; border-radius: 21px; background: linear-gradient(#4a4a4a, #111); box-shadow: 0 2px 3px rgba(0,0,0,0.35); color: #fff; font-weight: 700; font-size: 15px; line-height: 42px; padding-left: 17px; }
  .cta__arrow { position: absolute; left: 128px; top: 10px; }

  .footer { position: absolute; left: 0; top: 830px; width: 1200px; height: 298px; background: var(--footer-bg); }
  .footer__heading { position: absolute; font-family: "Arimo", sans-serif; font-size: 19px; color: var(--accent); }
  .footer__rule { position: absolute; left: 125px; top: 60px; width: 618px; height: 1px; background: #4a4a4a; }
  .link-col { position: absolute; top: 80px; list-style: none; font-size: 12px; letter-spacing: 0.3px; color: var(--footer-link); }
  .link-col li { height: 24px; line-height: 16px; }
  .link-col--divided { border-right: 1px solid var(--footer-rule); height: 184px; }

  .panel { position: absolute; left: 771px; top: 62px; width: 231px; height: 173px; background: var(--panel-bg); border: 1px solid var(--panel-border); border-radius: 3px; color: #fff; }
  .panel__title { position: absolute; left: 7px; font-size: 16px; }
  .search { position: absolute; left: 7px; top: 38px; width: 158px; height: 23px; background: #fff; border-radius: 3px; font-size: 12px; color: #aaa; padding: 4px 4px; }
  .search-go { position: absolute; left: 179px; top: 41px; font-size: 13px; text-decoration: underline; color: #ddd; display: flex; align-items: center; gap: 3px; }
  .panel__contact { position: absolute; left: 11px; top: 126px; font-size: 12px; line-height: 18px; }

  .legal { position: absolute; left: 0; top: 1128px; width: 1200px; height: 40px; background: var(--footer-deep); text-align: center; font-size: 9px; letter-spacing: 0.4px; color: #aaa; line-height: 46px; }
</style>
</head>
<body>
  <div class="topbar">
    <span class="topbar__contact">Demo User . (555) 014-2290 . info@brightcrate.example</span>
  </div>

  <header class="header">
    <div class="brand">
      <span class="brand__dot"></span>
      <span class="brand__name">BrightCrate Supply</span>
    </div>
  </header>

  <div class="stage"></div>
  <div class="banner" role="img" aria-label="Showcase of branded promotional products: cap, cooler bag, travel mug, sports bottle with sunglasses, and polo shirt">
    <div class="banner__shelf"></div>
  </div>
  <div class="banner__shadow"></div>

  <main class="intro">
    <h1 class="intro__title">Welcome To The Future of Promotional Products!</h1>
    <p class="intro__text">Gone are the days of searching through dog-eared catalogs or trying to make sense of complicated product websites.</p>
    <p class="intro__text">We do the work for you! We've taken only the very best and most current products and placed them in easy-to-use categories designed for your needs. Take a look at our selection - quality products at excellent prices.</p>
    <h2 class="intro__title intro__title--second">Enjoy This Amazing New Resource</h2>
    <p class="intro__text">We know you don't have time to waste; so we've cut to the chase and made it simple! But keep in mind, we do have access to over a million products - so if you don't see what you're looking for or have a special theme or request, let us know - we'll find it!</p>
  </main>

  <div class="cta">
    <a class="cta__button" href="#">Start shopping
      <svg class="cta__arrow" width="50" height="40" viewBox="0 0 50 40"><path d="M0 0 H50 L25 36 Z" fill="#1a1a1a"/><path d="M6 0 H44 L25 27 Z" fill="var(--accent)"/><path d="M19 6 H31 L25 13 Z" fill="#222"/></svg>
    </a>
  </div>

  <footer class="footer">
    <h3 class="footer__heading" style="left:123px;top:21px;">Shop By Category</h3>
    <h3 class="footer__heading" style="left:638px;top:23px;">Shop By Price</h3>
    <div class="footer__rule"></div>

    <ul class="link-col link-col--divided" style="left:124px;width:149px;">
      <li>Apparel</li><li>Bags &amp; Totes</li><li>Caps &amp; Hats</li><li>Computer</li><li>Eco Friendly</li><li>Food, Candy &amp; Drink</li><li>Golf, Sports &amp; Outdoors</li><li>Home &amp; Housewares</li>
    </ul>
    <ul class="link-col link-col--divided" style="left:294px;width:137px;">
      <li>Writing Instruments</li><li>Auto</li><li>Business Supplies</li><li>Clocks &amp; Watches</li><li>Corporate Gifts</li><li>Electronics</li><li>Games &amp; Novelties</li><li>Healthcare &amp; Safety</li>
    </ul>
    <ul class="link-col link-col--divided" style="left:450px;width:164px;">
      <li>Tradeshows &amp; Events</li><li>Awards &amp; Recognition</li><li>Calendars, Books &amp; Cards</li><li>Company Outings</li><li>Desktop &amp; Office</li><li>Executive Gifts</li><li>Gift Sets</li><li>Holiday</li>
    </ul>
    <ul class="link-col" style="left:640px;">
      <li>Under $5</li><li>$5 - $10</li><li>$10 - $20</li><li>$20 - $50</li><li>$50 - $100</li><li>$100 - $200</li><li>Over $200</li>
    </ul>

    <div class="panel">
      <div class="panel__title" style="top:6px;">Quick Search</div>
      <div class="search">search..</div>
      <a class="search-go" href="#">Go <svg width="13" height="12" viewBox="0 0 13 12"><path d="M0 0 L13 6 L0 12 Z" fill="var(--accent)"/></svg></a>
      <div class="panel__title" style="top:90px;">Contact Us</div>
      <div class="panel__contact">info@brightcrate.example<br>www.brightcrate.example</div>
    </div>
  </footer>

  <div class="legal">Copyright © 2010 . BrightCrate.example V3 . All Rights Reserved.</div>
</body>
</html>
```